Presentation Folder for Crest Holdings

We are a new property management / real estate company in Denver Colorado and are in need of new stationary design. Attached are our business card and logo deigns. We are looking for our stationary design. We need a presentation folder design that is Professional, exciting, and approachable. We do not have a preference on folder layout (pockets, style of folding) but will most likely be using a standard two pocket folder design (roughly 9x12) but feel free to experiment with and folder style as long as we can find a place to print them. We would also like to have a matching letterhead/page design
Below is standard size of folder from plume press
Full Bleed Size
20.87" x 16.68"
53 x 42.4 cm
6260 x 5004 pixels
Document Trim Size
20.75" x 16.56"
52.7 x 42.1 cm
6225 x 4969 pixels
Target Market(s)
We are attempting to target the top end of the real estate market in Denver Colorado. Are target market is investors in real estate.
Industry/Entity Type
Property Management
Font styles to use
Other font styles liked:
- Would like to keep font same to logo
Look and feel
Each slider illustrates characteristics of the customer's brand and the style your logo design should communicate.

```html
<!DOCTYPE html>
<html lang="en">
<head>
<meta charset="utf-8">
<title>Crest Holdings – Stationery</title>
<link href="https://fonts.googleapis.com/css2?family=Oswald:wght@500&family=Open+Sans:wght@400;600;700&family=Allura&display=swap" rel="stylesheet">
<style>
  :root{
    --blue:#4aa8c8;
    --blue-faint:#d3e7ee;
    --charcoal:#4b4b4d;
    --ink:#4a4a4a;
    --paper:#ffffff;
    --stage:#efefef;
    --rule-grey:#d6d6d6;
  }
  *{box-sizing:border-box;margin:0;padding:0}
  html,body{width:1200px;height:1000px;overflow:hidden}
  body{background:var(--stage);font-family:"Open Sans",Arial,sans-serif;color:var(--ink);position:relative}
  address{font-style:normal}
  .sheet{position:absolute;background:var(--paper);box-shadow:0 1px 3px rgba(0,0,0,.12);overflow:hidden}

  /* brand lockup */
  .brand{display:flex;flex-direction:column;align-items:flex-start}
  .brand-mark{border-radius:50%;background:var(--blue);margin-bottom:3px}
  .brand-name{font-family:"Oswald","Arial Narrow",sans-serif;font-weight:500;color:var(--blue);text-transform:uppercase;line-height:1;letter-spacing:.2px;white-space:nowrap}
  .brand-tag{color:var(--blue);line-height:1.2;white-space:nowrap}

  .contact{font-size:5px;line-height:1.45;color:var(--ink);white-space:nowrap}
  .contact strong{color:var(--blue);font-weight:700}

  /* letterhead */
  .letterhead{left:212px;top:125px;width:368px;height:520px}
  .letterhead .brand{position:absolute;left:46px;top:44px;align-items:center}
  .letterhead .brand-mark{width:22px;height:22px}
  .letterhead .brand-name{font-size:14px}
  .letterhead .brand-tag{font-size:5px}
  .letterhead .contact{position:absolute;left:262px;top:49px}
  .letter-body{position:absolute;left:46px;top:150px;width:280px;font-size:5.3px;line-height:1.6}
  .letter-body p{margin-bottom:11px}
  .signature{position:absolute;left:54px;top:402px;font-family:"Allura",cursive;font-size:20px;color:#222}
  .watermark{position:absolute;left:215px;top:368px;width:160px;height:160px;border-radius:50%;border:8px solid var(--rule-grey);background:var(--blue-faint);opacity:.7}

  /* folder */
  .folder{left:645px;top:100px;width:437px;height:548px;background:var(--charcoal)}
  .folder svg{position:absolute;inset:0}
  .folder .brand{position:absolute;left:178px;top:356px;align-items:center}
  .folder .brand-mark{width:22px;height:22px}
  .folder .brand-name{font-size:14px}
  .folder .brand-tag{font-size:5px}

  /* business cards */
  .card-front{left:82px;top:692px;width:164px;height:86px}
  .card-front .band{position:absolute;left:0;top:0;width:164px;height:56px}
  .card-front .brand{position:absolute;left:8px;top:62px;flex-direction:row;align-items:center;gap:4px}
  .card-front .brand-mark{width:16px;height:16px;margin:0}
  .card-front .brand-name{font-size:11px}
  .card-back{left:82px;top:815px;width:164px;height:91px}
  .card-back .brand{position:absolute;left:70px;top:8px;flex-direction:row;align-items:center;gap:4px}
  .card-back .brand-mark{width:14px;height:14px;margin:0}
  .card-back .brand-name{font-size:10px}
  .card-back .brand-tag{position:absolute;left:88px;top:22px;font-size:3.5px}
  .card-back .contact{font-size:4.3px;line-height:1.35}
  .person{position:absolute;left:6px;top:42px;font-size:4.5px;line-height:1.3}
  .person .name{color:var(--blue);font-weight:700;font-size:5.5px}
  .card-back .address{position:absolute;left:6px;top:66px}
  .card-back .web{position:absolute;left:92px;top:50px}
  .card-back .lines{position:absolute;left:92px;top:63px}

  /* envelopes */
  .envelope{left:291px;top:706px;width:411px;height:197px}
  .envelope .brand{position:absolute;left:22px;top:14px;align-items:center}
  .envelope .brand-mark{width:20px;height:20px}
  .envelope .brand-name{font-size:12px}
  .envelope .brand-tag{font-size:4.5px}
  .envelope .watermark{left:282px;top:96px;width:128px;height:128px;border-width:6px}
  .envelope .contact{position:absolute;left:328px;top:137px}
  .envelope-back{left:742px;top:706px;width:413px;height:197px}
  .envelope-back svg{position:absolute;inset:0}
  .envelope-back .brand{position:absolute;left:176px;top:18px;align-items:center}
  .envelope-back .brand-mark{width:16px;height:16px;background:var(--charcoal)}
  .envelope-back .brand-name{font-size:10px;color:var(--charcoal)}
  .envelope-back .brand-tag{font-size:4px;color:var(--charcoal)}
</style>
</head>
<body>

<section class="sheet letterhead" aria-label="Letterhead">
  <div class="brand">
    <span class="brand-mark"></span>
    <span class="brand-name">Crest Holdings</span>
    <span class="brand-tag">Property Management and Real Estate</span>
  </div>
  <address class="contact">
    <strong>CREST HOLDINGS</strong><br>P.O. BOX 4120<br>Denver, CO 80211<br>☏ 303 555 0142<br>✆ (720) 555 0188<br>✆ (720) 555 0129<br>✉ dana@crestholdingsco.com<br>www.crestholdingsco.com
  </address>
  <div class="letter-body">
    <p>Dear Client,</p>
    <p>Lorem ipsum dolor sit amet, consectetur adipiscing elit. Nulla sodales nisi vitae lorem ipsum dolor sit amet, consectetur adipiscing elit. Suspendisse feugiat eros nisl, a facilisis risus eleifend sed. Aliquam mauris enim, fermentum eu lacinia sit amet, laoreet eu leo. Nullam eleifend nulla in libero tristique, ac vulputate odio tincidunt. Etiam non condimentum tortor. Integer suscipit neque nec odio porttitor cursus. Phasellus a sapien blandit, suscipit justo id, condimentum ante. Morbi tristique justo risus, id mattis dui molestie ut. Nullam volutpat ut quam commodo faucibus. Pellentesque urna est, interdum in elit quis, pharetra elementum orci. Nam pharetra velit molestie justo placerat scelerisque.</p>
    <p>Nulla tincidunt molestie libero vel pretium. Donec condimentum nulla sit amet risus semper imperdiet. Duis congue eros nec diam blandit, et pellentesque sapien auctor. Curabitur iaculis enim lectus, in imperdiet mauris mattis eget. Etiam ac ornare metus. Mauris risus leo, egestas at dolor a, ultrices adipiscing est. Nunc faucibus scelerisque mollis. Pellentesque aliquet mauris tellus, id dignissim risus viverra et. Mauris venenatis lobortis eros. Nam id diam in ligula malesuada feugiat. Cras turpis felis, aliquet id mauris elementum, feugiat ultricies nisi.</p>
    <p>Nullam auctor venenatis metus, eu pulvinar sapien dapibus non. Cum sociis natoque penatibus et magnis dis parturient montes, nascetur ridiculus mus. Praesent sed lorem eget tortor volutpat dictum vel vel ipsum. Morbi ac mauris sed elit dictum volutpat. Morbi pulvinar non nisi in ultrices. Pellentesque quis mi in risus eleifend adipiscing.</p>
    <p>Best regards,</p>
  </div>
  <div class="signature">Dana Holt</div>
  <div class="watermark" aria-hidden="true"></div>
</section>

<section class="sheet folder" aria-label="Presentation folder">
  <svg width="437" height="548" viewBox="0 0 437 548" aria-hidden="true">
    <polygon points="0,0 437,0 437,200 0,262" fill="var(--blue)"/>
    <rect x="0" y="0" width="6" height="548" fill="rgba(0,0,0,.08)"/>
    <circle cx="222" cy="240" r="172" fill="#f4f4f4"/>
  </svg>
  <div class="brand">
    <span class="brand-mark"></span>
    <span class="brand-name">Crest Holdings</span>
    <span class="brand-tag">Property Management and Real Estate</span>
  </div>
</section>

<section class="sheet card-front" aria-label="Business card front">
  <svg class="band" viewBox="0 0 164 56" aria-hidden="true">
    <polygon points="0,0 164,0 164,56 0,40" fill="var(--blue)"/>
  </svg>
  <div class="brand">
    <span class="brand-mark"></span>
    <span class="brand-name">Crest Holdings</span>
  </div>
</section>

<section class="sheet card-back" aria-label="Business card back">
  <div class="brand">
    <span class="brand-mark"></span>
    <span class="brand-name">Crest Holdings</span>
  </div>
  <span class="brand-tag">Property Management and Real Estate</span>
  <div class="person"><div class="name">DANA HOLT</div>Owner/Broker</div>
  <address class="contact address"><strong>CREST HOLDINGS</strong><br>P.O. BOX 4120<br>Denver, CO 80211</address>
  <div class="contact web"><strong>www.crestholdingsco.com</strong></div>
  <div class="contact lines">☏ 303 555 0142<br>✆ (720) 555 0188<br>✆ (720) 555 0129<br>✉ dana@crestholdingsco.com</div>
</section>

<section class="sheet envelope" aria-label="Envelope front">
  <div class="brand">
    <span class="brand-mark"></span>
    <span class="brand-name">Crest Holdings</span>
    <span class="brand-tag">Property Management and Real Estate</span>
  </div>
  <div class="watermark" aria-hidden="true"></div>
  <address class="contact">
    <strong>CREST HOLDINGS</strong><br>P.O. BOX 4120<br>Denver, CO 80211<br>☏ 303 555 0142<br>✆ (720) 555 0188<br>✆ (720) 555 0129<br>✉ dana@crestholdingsco.com<br>www.crestholdingsco.com
  </address>
</section>

<section class="sheet envelope-back" aria-label="Envelope back">
  <svg width="413" height="197" viewBox="0 0 413 197" aria-hidden="true">
    <path d="M0,0 H413 V58 Q206,78 0,58 Z" fill="var(--blue)"/>
  </svg>
  <div class="brand">
    <span class="brand-mark"></span>
    <span class="brand-name">Crest Holdings</span>
    <span class="brand-tag">Property Management and Real Estate</span>
  </div>
</section>

</body>
</html>
```